Trifold Brochure needed for Elm Path Counseling

Hi! We need to have a trifold brochure made.

We would like to see brochure designs that use our logo colors, which are khaki, chocolate brown, and gray.

The brochure should be a modern design and please use your creativity.

Brochure is a trifold brochure, size is 8.5 x 11 and full color.

The following attachment has the content to be used in the trifold brochure, as well as some possible pictures. I have also attached our logo.

We would like to use file #2 for sure (picture number 27193540) and add the quote from her...

"At first, I was reluctant about going to ElmPath. Once I got there, I was glad I went. I learned a lot and was treated like family the whole time." Maren Colby

Requirements
Must have
• Our logo
• Information should be listed exactly as the attached document
• You must stick with our logo colors

```html
<!DOCTYPE html>
<html lang="en">
<head>
<meta charset="utf-8">
<title>ElmPath Counseling – Trifold Brochure</title>
<link href="https://fonts.googleapis.com/css2?family=Montserrat:ital,wght@0,200;0,300;0,400;0,700;1,300&display=swap" rel="stylesheet">
<style>
  :root {
    --backdrop: #5f6b70;
    --paper: #ffffff;
    --ink: #3f3b37;
    --khaki: #bfae84;
    --brown: #5b3a24;
    --dark-panel: #3d3a38;
    --dark-text: #e2ddd3;
    --photo-green-a: #9cbf6a;
    --photo-green-b: #c9a48f;
    --photo-sky-a: #6fa9e0;
    --photo-sky-b: #d8ad72;
    --photo-portrait-a: #8a9aa3;
    --photo-portrait-b: #50606b;
  }
  * { box-sizing: border-box; margin: 0; padding: 0; }
  html, body { width: 1200px; height: 891px; overflow: hidden; }
  body {
    background: var(--backdrop);
    font-family: "Montserrat", Arial, sans-serif;
    color: var(--ink);
    display: flex; align-items: center; justify-content: center;
  }
  .brochure {
    width: 1110px; height: 858px;
    display: grid; grid-template-columns: repeat(3, 1fr);
    background: var(--paper);
  }
  .panel { padding: 46px 38px 40px; position: relative; overflow: hidden; }
  .panel + .panel { border-left: 1px solid #e3e3e3; }

  .panel-title { display: flex; gap: 12px; align-items: stretch; margin-bottom: 18px; }
  .title-bar { width: 5px; background: var(--khaki); flex: none; }
  .title-main { font-weight: 200; font-size: 36px; line-height: 1; letter-spacing: 1px; white-space: nowrap; }
  .title-sub { font-weight: 300; font-size: 13px; letter-spacing: 1px; text-transform: uppercase; margin-top: 6px; color: var(--brown); white-space: nowrap; }

  .intro { font-style: italic; font-weight: 300; font-size: 12.5px; line-height: 1.45; margin-bottom: 18px; }
  .intro b { font-style: normal; font-weight: 700; }

  .photo { width: 100%; }
  .photo-couple { height: 240px; background: linear-gradient(135deg, var(--photo-green-a), var(--photo-green-b)); }
  .photo-beach { height: 210px; background: linear-gradient(180deg, var(--photo-sky-a) 0%, #d9e6f2 55%, var(--photo-sky-b) 100%); margin: 18px 0 26px; }
  .photo-portrait { height: 300px; background: linear-gradient(160deg, var(--photo-portrait-a), var(--photo-portrait-b)); }

  .points { list-style: none; margin-top: 30px; display: flex; flex-direction: column; gap: 28px; }
  .point { display: flex; gap: 10px; align-items: flex-start; font-size: 12.5px; line-height: 1.45; font-weight: 300; }
  .point-num { font-weight: 200; font-size: 40px; line-height: 0.9; min-width: 26px; color: var(--brown); }
  .point b { font-weight: 700; }

  .section-label { font-weight: 700; font-size: 11px; letter-spacing: 1px; text-transform: uppercase; margin-bottom: 10px; color: var(--brown); }

  .panel-dark { background: var(--dark-panel); color: var(--dark-text); padding: 0; display: flex; flex-direction: column; }
  .quote { padding: 34px 38px 0; }
  .quote-mark { display: block; width: 40px; height: 4px; background: var(--khaki); margin-bottom: 18px; }
  .quote-text { font-style: italic; font-weight: 300; font-size: 14px; line-height: 1.65; }
  .quote-author { margin-top: 16px; font-size: 12px; font-weight: 700; letter-spacing: 1px; text-transform: uppercase; color: var(--khaki); }

  .brand { margin-top: auto; padding: 0 38px 40px; display: flex; align-items: center; gap: 12px; }
  .brand-dot { width: 22px; height: 22px; border-radius: 50%; background: var(--khaki); flex: none; }
  .brand-name { font-size: 20px; font-weight: 300; letter-spacing: 1px; color: var(--khaki); }

  .panel-right .points { margin-top: 0; gap: 30px; }
</style>
</head>
<body>
  <main class="brochure">
    <section class="panel panel-left">
      <header class="panel-title">
        <span class="title-bar"></span>
        <div>
          <div class="title-main">ElmPath</div>
          <div class="title-sub">is a...</div>
        </div>
      </header>
      <p class="intro">...Pro-active Opioid Education, not for addicts or problem patients. <b>ElmPath</b> only sees <b>Good Patients</b>, because problem patients and addicts <b>do not</b> want education they only want pills.</p>
      <div class="photo photo-couple" role="img" aria-label="Smiling couple embracing outdoors in a sunny park"></div>
      <ol class="points">
        <li class="point"><span class="point-num">1</span><span><b>Good Patients</b> are Receptive to new information</span></li>
        <li class="point"><span class="point-num">2</span><span><b>"Education" Good Patients</b> need it the least! Therefore their minds are open and will soak it up the Most.</span></li>
        <li class="point"><span class="point-num">3</span><span>ElmPath will <b>Teach You</b> and Hopefully <b>You</b> will <b>Teach someone else</b>. Better than that, maybe <b>Your</b> Education will <b>Save someone else</b></span></li>
      </ol>
    </section>

    <section class="panel panel-dark">
      <div class="photo photo-portrait" role="img" aria-label="Portrait of a smiling woman outdoors"></div>
      <blockquote class="quote">
        <span class="quote-mark"></span>
        <p class="quote-text">"At first, I was reluctant about going to ElmPath. Once I got there, I was glad I went. I learned a lot and was treated like family the whole time."</p>
        <p class="quote-author">Maren Colby</p>
      </blockquote>
      <div class="brand">
        <span class="brand-dot"></span>
        <span class="brand-name">ElmPath Counseling</span>
      </div>
    </section>

    <section class="panel panel-right">
      <header class="panel-title">
        <span class="title-bar"></span>
        <div>
          <div class="title-main">WELCOME TO</div>
          <div class="title-sub">ElmPath Counseling!!!</div>
        </div>
      </header>
      <h2 class="section-label">Who we are and what we do</h2>
      <ol class="points">
        <li class="point"><span class="point-num">1</span><span>ElmPath Counseling provides pro-active opioid education to the Patient and a Risk Management service to the Physician.</span></li>
      </ol>
      <div class="photo photo-beach" role="img" aria-label="Couple walking along a sandy beach by the ocean"></div>
      <ol class="points">
        <li class="point"><span class="point-num">2</span><span>We believe it starts with giving Education to good patients and letting it trickle down to Patients and friends they know, who could use the information too.</span></li>
        <li class="point"><span class="point-num">3</span><span>ElmPath helps the physicians by ensuring that the Patients are fully Educated and taking more responsibility for their treatment.</span></li>
      </ol>
    </section>
  </main>
</body>
</html>
```